Software Company Business Card Design

We are looking for a business card design for a software, messaging & IT services company based in Australia.

Talvora Group is the holding company for 3 brands all offering technology based business solutions; Talvora, Brindle & Quillpad. Brand Identity = Friendly, Professional, Viable, Vibrant, Creative

We want our business card to reflect that we are an innovative market leader. The design should be clean, professional and original.

This design will be used for all 3 brands.

More information about our company can be found at: www.talvoragroup.example.au
www.brindle.example.au

Details we would like on the card:

Firstname Lastname
Position
Level 17, 482 Ormond Rd
North Sydney
NSW 2060
Phone: +61 2 5550 1738
Fax: +61 2 5550 1794
Mobile:
Email:
www.talvoragroup.example.au

Target Market(s)

Our business cards are given to B2B and industry professionals.

Industry/Entity Type

Business

Requirements
Must have
• The Business Card must include the same colours as the logo.
Nice to have
• We would like it to me double sided.

```html
<!DOCTYPE html>
<html lang="en">
<head>
<meta charset="utf-8">
<title>Talvora Group – Business Card</title>
<link rel="stylesheet" href="https://fonts.googleapis.com/css2?family=Mulish:wght@400;600;700;800&display=swap">
<style>
  :root {
    --stage: #161616;
    --card-deep: #a30d33;
    --card-mid: #bd0f3d;
    --card-glow: #dc1b4c;
    --ink: #ffffff;
    --ink-soft: #f1e9ee;
    --accent-lilac: #b9b3d8;
    --watermark: rgba(120, 10, 40, 0.45);
  }
  * { margin: 0; padding: 0; box-sizing: border-box; }
  html, body {
    width: 1200px;
    height: 923px;
    overflow: hidden;
    background: var(--stage);
    font-family: "Mulish", "Trebuchet MS", sans-serif;
    color: var(--ink);
  }
  .stage { position: relative; width: 1200px; height: 923px; }

  .card {
    position: absolute;
    overflow: hidden;
    background:
      radial-gradient(circle at 62% 45%, rgba(230, 30, 80, 0.55) 0, rgba(230, 30, 80, 0) 45%),
      linear-gradient(135deg, var(--card-mid) 0%, var(--card-deep) 100%);
  }

  /* Front */
  .card--front { left: 130px; top: 363px; width: 563px; height: 337px; }
  .card--front::before {
    content: "";
    position: absolute;
    left: 400px; top: 220px;
    width: 260px; height: 260px;
    border-radius: 50%;
    background: radial-gradient(circle, rgba(225, 30, 75, 0.5) 0, rgba(225, 30, 75, 0) 70%);
  }
  .brand {
    position: absolute;
    left: 216px; top: 100px;
    width: 294px;
    font-weight: 600;
    color: var(--ink-soft);
    line-height: 1;
  }
  .brand__name { display: block; font-size: 72px; letter-spacing: 0.5px; }
  .brand__group { display: block; font-size: 30px; text-align: right; margin-top: 0; }
  .website {
    position: absolute;
    left: 218px; top: 262px;
    font-size: 21px;
    font-weight: 700;
    letter-spacing: 0.2px;
  }

  /* Back */
  .card--back {
    left: 713px; top: 138px; width: 337px; height: 562px;
    background:
      radial-gradient(circle at 15% 42%, rgba(230, 30, 80, 0.6) 0, rgba(230, 30, 80, 0) 45%),
      radial-gradient(circle at 80% 95%, rgba(220, 30, 75, 0.35) 0, rgba(220, 30, 75, 0) 35%),
      linear-gradient(160deg, var(--card-mid) 0%, var(--card-deep) 100%);
  }
  .watermark {
    position: absolute;
    left: 42px; top: 162px;
    width: 252px;
    font-weight: 600;
    color: var(--watermark);
    line-height: 1;
  }
  .watermark__name { display: block; font-size: 62px; letter-spacing: 0.5px; }
  .watermark__group { display: block; font-size: 26px; text-align: right; }

  .contact { position: absolute; left: 46px; top: 325px; }
  .contact__name { font-size: 22px; font-weight: 700; line-height: 1.1; }
  .contact__role { font-size: 16px; font-weight: 700; color: var(--accent-lilac); margin-bottom: 14px; }
  .contact__line { font-size: 17px; font-weight: 700; line-height: 23px; }
  .contact__line--small { font-size: 14px; line-height: 18px; margin-top: 2px; }
  .contact__label { font-size: 17px; }
</style>
</head>
<body>
  <main class="stage">
    <section class="card card--front" aria-label="Business card front">
      <div class="brand">
        <span class="brand__name">talvora</span>
        <span class="brand__group">group</span>
      </div>
      <p class="website">www.talvoragroup.example.au</p>
    </section>

    <section class="card card--back" aria-label="Business card back">
      <div class="watermark" aria-hidden="true">
        <span class="watermark__name">talvora</span>
        <span class="watermark__group">group</span>
      </div>
      <div class="contact">
        <p class="contact__name">Firstname Lastname</p>
        <p class="contact__role">position</p>
        <p class="contact__line">P: +61 2 5550 1738</p>
        <p class="contact__line">F: +61 2 5550 1794</p>
        <p class="contact__line contact__line--small"><span class="contact__label">A:</span> Level 17, 482 Ormond Rd West<br>Marrowdale NSW 2189</p>
      </div>
    </section>
  </main>
</body>
</html>
```